Hedge fund needs power point design for marketing pitch

We need a designer to make our power point pitch more aesthetically appealing to potential clients. We will be marketing our hedge fund to high net worth individuals and financial institutions. The ideal design will look professional and project confidence to our potential clients. We have attached a rough outline of what we have completed so far. We have also attached example cover pages for 2 pitch books produced by our competitors.

Target Market(s)

Financial institutions and wealthy investors

Industry/Entity Type

Finance

Requirements
Must have
• must use our logo and current slides. Must look professional

```html
<!DOCTYPE html>
<html lang="en">
<head>
<meta charset="utf-8">
<title>Investment Strategy</title>
<link rel="stylesheet" href="https://fonts.googleapis.com/css2?family=Jost:wght@400&family=Encode+Sans+Condensed:wght@600&display=swap">
<style>
  :root {
    --slide-bg: #ffffff;
    --title-teal: #2f9fa6;
    --body-ink: #1d3447;
    --bullet-teal: #3aa7ae;
    --photo-deep: #0f3a4a;
    --photo-mid: #3f8797;
    --photo-light: #a9d3da;
  }
  html, body {
    margin: 0;
    padding: 0;
    width: 1200px;
    height: 675px;
    overflow: hidden;
    background: var(--slide-bg);
  }
  .slide {
    position: relative;
    width: 1200px;
    height: 675px;
    overflow: hidden;
    background: var(--slide-bg);
  }
  .hero-visual {
    position: absolute;
    left: 0;
    top: 0;
    width: 569px;
    height: 675px;
    background:
      radial-gradient(ellipse at 30% 40%, var(--photo-light) 0%, rgba(169,211,218,0) 45%),
      linear-gradient(135deg, var(--photo-deep) 0%, var(--photo-mid) 55%, var(--photo-light) 100%);
  }
  .slide-title {
    position: absolute;
    left: 569px;
    right: 0;
    top: 22px;
    margin: 0;
    text-align: center;
    font-family: "Jost", sans-serif;
    font-weight: 400;
    font-size: 43px;
    letter-spacing: -0.5px;
    color: var(--title-teal);
  }
  .strategy-points {
    font-family: "Encode Sans Condensed", sans-serif;
    font-weight: 600;
    font-size: 20px;
    color: var(--body-ink);
    letter-spacing: -0.3px;
  }
  .line {
    position: absolute;
    white-space: nowrap;
    line-height: 1;
  }
  .point { left: 585px; }
  .point::before {
    content: "";
    display: inline-block;
    width: 6px;
    height: 6px;
    border-radius: 50%;
    background: var(--bullet-teal);
    margin-right: 3px;
    vertical-align: 6px;
  }
  .point-cont { left: 585px; }
  .sub-point { left: 682px; }
  .sub-point::before {
    content: "";
    position: absolute;
    left: -32px;
    top: 10px;
    width: 16px;
    height: 1.5px;
    background: var(--body-ink);
  }
  .sub-cont { left: 682px; }
</style>
</head>
<body>
  <main class="slide">
    <div class="hero-visual" role="img" aria-label="Photograph of a businessman touching a glowing digital financial chart with bars and a world map"></div>

    <h1 class="slide-title">Investment Strategy</h1>

    <section class="strategy-points">
      <div class="line point" style="top:103px">Strategy derived from a dynamic optimization problem</div>
      <div class="line point-cont" style="top:149px">that maximizes returns within a given risk constraint.</div>
      <div class="line point" style="top:195px">Parameters/assumptions</div>
      <div class="line sub-point" style="top:246px">Assume liquid markets</div>
      <div class="line sub-point" style="top:296px">Assume a price discount/premium on each</div>
      <div class="line sub-cont" style="top:334px">trade (5-10%)</div>
      <div class="line point" style="top:389px">&nbsp;Solution &ndash; the optimization problem tells us:</div>
      <div class="line sub-point" style="top:439px">When to buy or sell contracts</div>
      <div class="line sub-point" style="top:488px">Which contracts to buy or sell</div>
      <div class="line sub-point" style="top:539px">How many contracts to buy or sell</div>
      <div class="line point" style="top:590px">We make trades based on these solutions while hitting</div>
      <div class="line point-cont" style="top:635px">the price discount/premium offered by the market.</div>
    </section>
  </main>
</body>
</html>
```